Business Card for a new businees.

need a very good business for a new company based in Riverside California call Levy Lantern LLC. We help client file taxes, resolve tax debt and attain peace of mind We help people nationwide solve Tax problems. We help with Installment agreements, Offers in Compromise, Partial Pay Installment Agreements, Currently Not Collectible status, Liens and Levy Removal, Garnishment removal. We offer individualized services

Target Market(s)

Any one with Tax Problems nationwide. My clients span across age, occupation etc

Contact Information for Business Card

Card must be attractive and have enough information to let client know we care and call us

Colors

Designer to choose colors to be used in the design.

Requirements
Must have
• the basics and then surprise me
Nice to have
• surprise m

```html
<!DOCTYPE html>
<html lang="en">
<head>
<meta charset="utf-8">
<title>Levy Lantern LLC – Business Card</title>
<link rel="stylesheet" href="https://fonts.googleapis.com/css2?family=Poppins:wght@500;600&family=Work+Sans:wght@400;500&display=swap">
<style>
  :root {
    --backdrop: #3b3530;
    --card-dark: #1f1c1d;
    --card-light: #ffffff;
    --gold: #c9a227;
    --gold-deep: #a8881e;
    --ink: #1d1d1d;
  }
  html, body {
    margin: 0;
    padding: 0;
    width: 1200px;
    height: 930px;
    overflow: hidden;
    background: var(--backdrop);
  }
  .canvas {
    position: relative;
    width: 1200px;
    height: 930px;
  }
  .card {
    position: absolute;
    width: 700px;
    height: 400px;
    border-radius: 22px;
    box-shadow: 0 14px 30px rgba(0,0,0,0.35);
    overflow: hidden;
  }
  .card--front { left: 150px; top: 40px; background: var(--card-dark); }
  .card--back  { left: 350px; top: 490px; background: var(--card-light); }

  .brand {
    position: absolute;
    display: flex;
    align-items: center;
    gap: 16px;
  }
  .brand__dot {
    flex: none;
    border-radius: 50%;
    background: var(--gold);
  }
  .brand__name {
    font-family: "Poppins", sans-serif;
    font-weight: 600;
    color: var(--gold);
    line-height: 1;
    white-space: nowrap;
  }

  .card--front .brand { left: 180px; top: 168px; }
  .card--front .brand__dot { width: 56px; height: 56px; }
  .card--front .brand__name { font-size: 48px; }

  .card--back .brand { left: 60px; top: 78px; }
  .card--back .brand__dot { width: 40px; height: 40px; }
  .card--back .brand__name { font-size: 32px; }

  .person {
    position: absolute;
    right: 70px;
    top: 194px;
    text-align: right;
  }
  .person__name {
    font-family: "Poppins", sans-serif;
    font-weight: 500;
    font-size: 30px;
    color: var(--gold-deep);
    line-height: 1;
  }
  .divider {
    position: absolute;
    left: 200px;
    top: 234px;
    width: 430px;
    height: 2px;
    background: var(--gold-deep);
  }
  .person__title {
    position: absolute;
    right: 70px;
    top: 240px;
    font-family: "Work Sans", sans-serif;
    font-size: 15px;
    color: var(--ink);
  }
  .address {
    position: absolute;
    right: 70px;
    top: 272px;
    text-align: right;
    font-family: "Work Sans", sans-serif;
    font-size: 15px;
    line-height: 1.4;
    color: var(--ink);
  }
  .contacts {
    position: absolute;
    left: 200px;
    top: 276px;
    margin: 0;
    padding: 0;
    list-style: none;
    font-family: "Work Sans", sans-serif;
    font-size: 16px;
    color: var(--ink);
  }
  .contacts li { display: flex; align-items: center; gap: 10px; line-height: 1.55; }
  .contacts svg { width: 12px; height: 12px; flex: none; }
  .contacts .accent { color: var(--gold-deep); }
</style>
</head>
<body>
<main class="canvas">

  <section class="card card--front" aria-label="Card front">
    <div class="brand">
      <span class="brand__dot"></span>
      <span class="brand__name">Levy Lantern</span>
    </div>
  </section>

  <section class="card card--back" aria-label="Card back">
    <div class="brand">
      <span class="brand__dot"></span>
      <span class="brand__name">Levy Lantern</span>
    </div>

    <div class="person">
      <div class="person__name">Daniel Reyes</div>
    </div>
    <div class="divider"></div>
    <div class="person__title">Director</div>

    <div class="address">
      4260 Orchard Ave. Ste 310<br>
      Riverside, CA 92501
    </div>

    <ul class="contacts">
      <li>
        <svg viewBox="0 0 16 16" aria-hidden="true"><path fill="#a8881e" d="M3.6 1.2l2.3 2.7-1.3 1.9c.9 2 2.6 3.7 4.6 4.6l1.9-1.3 2.7 2.3-1.2 2.4C7.4 13.6 2.4 8.6 1.2 3.4z"/></svg>
        951-555-0148
      </li>
      <li>
        <svg viewBox="0 0 16 16" aria-hidden="true"><rect x="1.5" y="3.5" width="13" height="9" fill="none" stroke="#a8881e" stroke-width="1.5"/><path d="M1.5 3.5L8 9l6.5-5.5" fill="none" stroke="#a8881e" stroke-width="1.5"/></svg>
        info@levylantern.com
      </li>
      <li>
        <svg viewBox="0 0 16 16" aria-hidden="true"><circle cx="8" cy="8" r="6.5" fill="none" stroke="#a8881e" stroke-width="1.4"/><ellipse cx="8" cy="8" rx="2.8" ry="6.5" fill="none" stroke="#a8881e" stroke-width="1.2"/><path d="M1.5 8h13" stroke="#a8881e" stroke-width="1.2"/></svg>
        <span>www.<span class="accent">levylantern</span>.com</span>
      </li>
    </ul>
  </section>

</main>
</body>
</html>
```